Marlow Hire Business Card for recruitment company

We are looking for a Business Card Design that incorporates our personal details and our busines name and logo. We are a specialized search consultancy that recruit Property and Construction professionals.
We would like a business card that stands out and is appealing to the Construction and Property industry as well.

Target Market(s)

people in the construction and property industry

Contact Information for Business Card

Business Name and logo

Font styles to use
Serif

Colors
0094D4
00A9DD
6FCCEA
C7EBF8
E9F6FB

Requirements
Must have
• Business name and logo as well as contact details
Should not have
• No photos of us please

```html
<!DOCTYPE html>
<html lang="en">
<head>
<meta charset="utf-8">
<title>Marlow Hire Business Card</title>
<link rel="stylesheet" href="https://fonts.googleapis.com/css2?family=Libre+Baskerville:wght@400;700&display=swap">
<style>
  :root {
    --backdrop: #cfcfcf;
    --card: #ffffff;
    --brand-deep: #0b5f86;
    --brand: #0094d4;
    --brand-bright: #00a9dd;
    --brand-soft: #6fccea;
    --brand-pale: #c7ebf8;
    --brand-mist: #e9f6fb;
    --ink: #2b2b2b;
    --muted: #555555;
    --rule: #9ccfe2;
    --white: #ffffff;
  }
  html, body {
    margin: 0;
    padding: 0;
    width: 900px;
    height: 1200px;
    overflow: hidden;
    background: var(--backdrop);
    font-family: "Libre Baskerville", Georgia, serif;
  }
  .canvas { position: relative; width: 900px; height: 1200px; }
  .card {
    position: absolute;
    left: 79px;
    width: 743px;
    height: 441px;
    overflow: hidden;
  }
  .card--front { top: 131px; background: var(--card); }
  .card--back {
    top: 638px;
    background: var(--brand-deep);
    display: flex;
    align-items: center;
    justify-content: center;
  }

  .brand {
    display: flex;
    align-items: center;
    white-space: nowrap;
  }
  .brand__mark { flex: none; border-radius: 50%; }
  .brand__name {
    font-weight: 400;
    text-transform: uppercase;
    letter-spacing: 2px;
    line-height: 1;
  }

  .card--front .brand {
    position: absolute;
    top: 62px;
    right: 45px;
  }
  .card--front .brand__mark {
    width: 38px; height: 38px;
    margin-right: 14px;
    background: var(--brand-bright);
  }
  .card--front .brand__name { font-size: 38px; color: var(--brand-deep); }

  .card--back .brand { margin-top: 8px; }
  .card--back .brand__mark {
    width: 52px; height: 52px;
    margin-right: 20px;
    background: var(--brand-soft);
  }
  .card--back .brand__name { font-size: 52px; color: var(--white); }

  .holder { position: absolute; left: 50px; top: 226px; }
  .holder__name {
    margin: 0;
    font-size: 23px;
    font-weight: 700;
    color: var(--brand-deep);
    line-height: 1.2;
  }
  .holder__role { margin: 4px 0 0; font-size: 14px; color: var(--muted); }

  .divider {
    position: absolute;
    left: 50px; top: 288px;
    width: 658px; height: 1px;
    background: var(--rule);
  }

  .contacts {
    position: absolute;
    left: 50px; top: 300px;
    margin: 0; padding: 0;
    list-style: none;
    font-size: 14.5px;
    color: var(--ink);
  }
  .contacts li { display: flex; align-items: center; height: 24.5px; }
  .contacts svg {
    width: 14px; height: 14px;
    margin-right: 17px;
    fill: var(--brand);
    stroke: none;
  }

  .address {
    position: absolute;
    left: 496px; top: 330px;
    margin: 0;
    font-size: 14.5px;
    font-style: normal;
    line-height: 22px;
    color: var(--ink);
  }

  .swoosh { position: absolute; left: 0; bottom: 0; width: 743px; height: 60px; }
</style>
</head>
<body>
<main class="canvas">
  <section class="card card--front">
    <div class="brand">
      <span class="brand__mark" aria-hidden="true"></span>
      <span class="brand__name">Marlow Hire</span>
    </div>

    <div class="holder">
      <h1 class="holder__name">Dana Whitlock</h1>
      <p class="holder__role">Owner/ Designer</p>
    </div>

    <div class="divider"></div>

    <ul class="contacts">
      <li>
        <svg viewBox="0 0 16 16" aria-hidden="true"><path d="M1 6c0-2 3-4 7-4s7 2 7 4v1h-4V5.5H5V7H1z"/><path d="M3 8h10l1 6H2z"/></svg>
        (555) 014-2290
      </li>
      <li>
        <svg viewBox="0 0 16 16" aria-hidden="true"><path d="M1 4h14v1.2L8 9.5 1 5.2z"/><path d="M1 6.8l7 4.3 7-4.3V13H1z"/></svg>
        info@marlowhire.com
      </li>
      <li>
        <svg viewBox="0 0 16 16" aria-hidden="true"><path d="M8 1a7 7 0 1 0 0 14A7 7 0 0 0 8 1zm0 1.6c.9 0 1.9 1.9 2.1 4.6H5.9C6.1 4.5 7.1 2.6 8 2.6zM2.7 7.2h1.8c.1-1.4.4-2.7.9-3.6a5.4 5.4 0 0 0-2.7 3.6zm0 1.6a5.4 5.4 0 0 0 2.7 3.6c-.5-.9-.8-2.2-.9-3.6zm3.2 0h4.2c-.2 2.7-1.2 4.6-2.1 4.6s-1.9-1.9-2.1-4.6zm5.6 0c-.1 1.4-.4 2.7-.9 3.6a5.4 5.4 0 0 0 2.7-3.6zm1.8-1.6a5.4 5.4 0 0 0-2.7-3.6c.5.9.8 2.2.9 3.6z"/></svg>
        www.marlowhire.com
      </li>
    </ul>

    <address class="address">82 Harbor Lane<br>Bayview, CA 90012</address>

    <svg class="swoosh" viewBox="0 381 743 60" preserveAspectRatio="none" aria-hidden="true">
      <path fill="var(--brand-soft)" d="M8 441 C150 408 350 391 525 389 C380 393 250 408 120 441 Z"/>
      <path fill="var(--brand-deep)" d="M135 441 C260 412 400 400 540 399 L743 399 L743 441 Z"/>
    </svg>
  </section>

  <section class="card card--back">
    <div class="brand">
      <span class="brand__mark" aria-hidden="true"></span>
      <span class="brand__name">Marlow Hire</span>
    </div>
  </section>
</main>
</body>
</html>
```